Veltrano - Mechanic/Collision Center Business Card

We're looking for a business card design for our mechanic/ collision repair shop.

Can be with colours or monochromatic.

See the attached files.

Many thanks

```html
<!DOCTYPE html>
<html lang="en">
<head>
<meta charset="utf-8">
<title>Veltrano – Business Card</title>
<link rel="stylesheet" href="https://fonts.googleapis.com/css2?family=Lato:wght@400;700;900&display=swap">
<style>
  :root {
    --page-bg: #d9d9d9;
    --card-light: #f4f3ee;
    --card-dark: #1b1d1e;
    --ink: #232323;
    --accent: #1e9ad6;
    --cream: #ece8da;
  }
  * { box-sizing: border-box; margin: 0; padding: 0; }
  html, body { width: 1200px; height: 787px; overflow: hidden; }
  body {
    background: var(--page-bg);
    font-family: "Lato", Arial, sans-serif;
    color: var(--ink);
    position: relative;
  }
  .card {
    position: absolute;
    top: 219px;
    width: 540px;
    height: 348px;
    border-radius: 3px;
    box-shadow: 0 6px 18px rgba(0,0,0,0.18);
  }
  .card-front { left: 40px; background: var(--card-light); }
  .card-back { left: 620px; background: var(--card-dark); }

  .brand {
    position: absolute;
    display: flex;
    align-items: center;
    gap: 10px;
    font-weight: 900;
    letter-spacing: 1px;
    text-transform: uppercase;
  }
  .brand-dot { border-radius: 50%; flex: none; }

  .card-front .brand {
    left: 30px; top: 150px;
    font-size: 33px;
    color: var(--ink);
  }
  .card-front .brand-dot { width: 22px; height: 22px; background: var(--accent); }

  .divider {
    position: absolute;
    left: 262px; top: 64px;
    width: 1.5px; height: 226px;
    background: var(--accent);
  }

  .contact {
    position: absolute;
    left: 280px; top: 68px;
    width: 250px;
    font-size: 14.5px;
    line-height: 1.5;
  }
  .contact-name {
    font-size: 26px;
    font-weight: 700;
    color: var(--accent);
    line-height: 1.1;
  }
  .contact-role { margin-bottom: 2px; }
  .contact-row { display: flex; align-items: center; gap: 7px; }
  .contact-row svg { flex: none; }
  .label { color: var(--accent); }
  .details { margin-top: 8px; }
  .links { margin-top: 8px; }
  .social-dot {
    width: 12px; height: 12px; border-radius: 50%;
    background: var(--accent); flex: none;
  }

  .card-back .brand {
    left: 50%; top: 50%;
    transform: translate(-50%, -50%);
    font-size: 48px;
    color: var(--cream);
  }
  .card-back .brand-dot { width: 30px; height: 30px; background: var(--cream); }
</style>
</head>
<body>

  <section class="card card-front" aria-label="Business card front">
    <div class="brand"><span class="brand-dot"></span>Veltrano</div>

    <div class="divider"></div>

    <div class="contact">
      <p class="contact-name">Tomás Vidrelo</p>
      <p class="contact-role">Manager Director</p>
      <p class="contact-row">
        <svg width="12" height="12" viewBox="0 0 24 24" aria-hidden="true"><path fill="var(--accent)" d="M6.6 10.8a15.1 15.1 0 0 0 6.6 6.6l2.2-2.2a1 1 0 0 1 1-.25 11.4 11.4 0 0 0 3.6.57 1 1 0 0 1 1 1V20a1 1 0 0 1-1 1A17 17 0 0 1 3 4a1 1 0 0 1 1-1h3.5a1 1 0 0 1 1 1c0 1.25.2 2.45.57 3.57a1 1 0 0 1-.25 1z"/></svg>
        +351 912 480 375
      </p>

      <div class="details">
        <p><span class="label">Name:</span> Veltrano, LDA</p>
        <p><span class="label">Address:</span> Rua das Oficinas, 42</p>
        <p><span class="label">Postal code:</span> 1900-118 Lisboa</p>
      </div>

      <div class="links">
        <p class="contact-row">
          <svg width="12" height="12" viewBox="0 0 24 24" aria-hidden="true"><path fill="var(--accent)" d="M6.6 10.8a15.1 15.1 0 0 0 6.6 6.6l2.2-2.2a1 1 0 0 1 1-.25 11.4 11.4 0 0 0 3.6.57 1 1 0 0 1 1 1V20a1 1 0 0 1-1 1A17 17 0 0 1 3 4a1 1 0 0 1 1-1h3.5a1 1 0 0 1 1 1c0 1.25.2 2.45.57 3.57a1 1 0 0 1-.25 1z"/></svg>
          +351 213 570 846
        </p>
        <p class="contact-row">
          <svg width="12" height="10" viewBox="0 0 24 18" aria-hidden="true"><rect x="1" y="1" width="22" height="16" fill="var(--accent)"/><path d="M1 1l11 9 11-9" fill="none" stroke="var(--card-light)" stroke-width="2"/></svg>
          oficina@veltrano.pt
        </p>
        <p class="contact-row"><span class="social-dot"></span>www.veltrano.pt/social</p>
      </div>
    </div>
  </section>

  <section class="card card-back" aria-label="Business card back">
    <div class="brand"><span class="brand-dot"></span>Veltrano</div>
  </section>

</body>
</html>
```